Hollowbrook Leasing Business Card Design

Need business cards designed for our new equipment rental. We specialize in renting to landscape / tree professionals, contractors, Do-It-Yourself'ers and Around the home or office. Looking for a eye catching card. Landscape and construction should be the theme. The logo is attached, and you can see our colors from the logo. You can use whatever color goes with it ok.

Target Market(s)

First off Landscape and Tree Professional. Then contractors, Do-It-Yourself'ers and rentals for Around the home or office.

Industry/Entity Type

Business

Contact Information for Business Card

Eye catching background that blends landscaping with construction equipment

Requirements
Must have
• Name on Card will Be: Derek Tollund (Manager)
• My Direct Phone Number is: 352-715-3092
• derek@hollowbrookleasing.example
• www.hollowbrookleasing.example
• 4172 Marsh Wren Lane,
• Dade City FL 33519
Nice to have
• Would be Nice to have these bullets on the Face of the card that does not have all my information.
• Serving:
• Landscape / Tree Professionals
• Contractors
• DYI'ers or say Do-It-Yourself'ers
• Maybe have serving small and centered above these bullets, and these 3 bullets along the bottom of the card. Ideas?

```html
<!DOCTYPE html>
<html lang="en">
<head>
<meta charset="utf-8">
<title>Hollowbrook Leasing Business Card</title>
<link rel="stylesheet" href="https://fonts.googleapis.com/css2?family=Roboto:wght@400;500;700;900&display=swap">
<style>
  :root {
    --page-bg: #e4e4e2;
    --frost-light: #eef0f1;
    --frost-mid: #d3d7da;
    --brand-navy: #1b2a3c;
    --text-white: #f4f6f9;
    --text-soft: #d9dfe7;
    --email-tint: #f2c6c1;
  }
  html, body {
    margin: 0;
    padding: 0;
    width: 1200px;
    height: 969px;
    overflow: hidden;
    background: var(--page-bg);
    font-family: "Roboto", Arial, sans-serif;
  }
  .card {
    position: absolute;
    left: 100px;
    top: 199px;
    width: 1000px;
    height: 571px;
    overflow: hidden;
    background: linear-gradient(135deg, var(--frost-light) 0%, var(--frost-mid) 55%, #e6e9eb 100%);
    box-shadow: 0 10px 30px rgba(0,0,0,0.18);
  }
  .card-shapes {
    position: absolute;
    inset: 0;
  }
  .contact {
    position: absolute;
    left: 48px;
    top: 0;
    color: var(--text-white);
  }
  .contact-name {
    position: absolute;
    top: 196px;
    margin: 0;
    font-size: 31px;
    font-weight: 500;
    letter-spacing: 0.5px;
    white-space: nowrap;
  }
  .contact-title {
    position: absolute;
    top: 243px;
    margin: 0;
    font-size: 24px;
    font-weight: 400;
    color: var(--text-soft);
    white-space: nowrap;
  }
  .contact-address {
    position: absolute;
    top: 295px;
    margin: 0;
    font-size: 23px;
    line-height: 31px;
    font-style: normal;
    color: var(--text-soft);
    white-space: nowrap;
  }
  .contact-lines {
    position: absolute;
    top: 374px;
    margin: 0;
    padding: 0;
    list-style: none;
  }
  .contact-lines li {
    display: flex;
    align-items: center;
    height: 31.7px;
    font-size: 22px;
    color: var(--text-soft);
    white-space: nowrap;
  }
  .contact-lines svg {
    width: 20px;
    height: 20px;
    margin: 0 20px 0 4px;
    fill: var(--text-soft);
  }
  .contact-lines .email { color: var(--email-tint); }
  .contact-lines .web { color: var(--text-white); }
  .brand {
    position: absolute;
    left: 524px;
    top: 150px;
    width: 420px;
    display: flex;
    align-items: center;
    gap: 16px;
  }
  .brand-mark {
    flex: none;
    width: 30px;
    height: 30px;
    background: var(--brand-navy);
  }
  .brand-name {
    margin: 0;
    font-size: 44px;
    line-height: 1.08;
    font-weight: 900;
    letter-spacing: 0.5px;
    text-transform: uppercase;
    color: var(--brand-navy);
  }
</style>
</head>
<body>
  <main class="card">
    <svg class="card-shapes" width="1000" height="571" viewBox="0 0 1000 571" aria-hidden="true">
      <defs>
        <linearGradient id="panelGradient" x1="0" y1="0" x2="1" y2="1">
          <stop offset="0" stop-color="#2a4466"/>
          <stop offset="0.45" stop-color="#1d3656"/>
          <stop offset="1" stop-color="#0d1c31"/>
        </linearGradient>
        <linearGradient id="silverEdge" x1="0" y1="0" x2="0" y2="1">
          <stop offset="0" stop-color="#eef1f4"/>
          <stop offset="0.5" stop-color="#9aa3ad"/>
          <stop offset="1" stop-color="#dfe3e7"/>
        </linearGradient>
      </defs>
      <polygon points="0,0 282,0 658,571 0,571" fill="#b9c0c8"/>
      <polygon class="panel" points="0,0 268,0 640,571 0,571" fill="url(#panelGradient)"/>
      <line x1="278" y1="0" x2="652" y2="571" stroke="url(#silverEdge)" stroke-width="6"/>
    </svg>

    <section class="contact">
      <h1 class="contact-name">DEREK TOLLUND</h1>
      <p class="contact-title">MANAGER</p>
      <address class="contact-address">4172 Marsh Wren Lane<br>Dade City, Florida 33519</address>
      <ul class="contact-lines">
        <li><svg viewBox="0 0 20 20"><path d="M4 2h4l1.5 4-2.2 1.6a11 11 0 0 0 5.1 5.1L14 10.5l4 1.5v4a2 2 0 0 1-2 2A14 14 0 0 1 2 4a2 2 0 0 1 2-2z"/></svg>352 715 3092</li>
        <li><svg viewBox="0 0 20 20"><path d="M6 1h8a1.5 1.5 0 0 1 1.5 1.5v15A1.5 1.5 0 0 1 14 19H6a1.5 1.5 0 0 1-1.5-1.5v-15A1.5 1.5 0 0 1 6 1zm0.5 2.5v11h7v-11zM10 15.5a1 1 0 1 0 0 2 1 1 0 0 0 0-2z"/></svg>352 804 1176</li>
        <li><svg viewBox="0 0 20 20"><path d="M5 1h10v5H5zM2 7h16v8h-3v4H5v-4H2zm5 6v4h6v-4z"/></svg>352 391 5028</li>
        <li class="email"><svg viewBox="0 0 20 20"><path d="M2 5h16v11H2zm1.5 1.5v.6L10 11l6.5-3.9v-.6z"/></svg>derek@hollowbrookleasing.example</li>
        <li class="web"><svg viewBox="0 0 20 20"><path d="M10 1.5a8.5 8.5 0 1 0 0 17 8.5 8.5 0 0 0 0-17zm5.8 5.5h-2.6a12 12 0 0 0-1.2-3.6A7 7 0 0 1 15.8 7zM10 3.2c.7 1 1.3 2.3 1.6 3.8H8.4c.3-1.5.9-2.8 1.6-3.8zM3.4 11.5a7 7 0 0 1 0-3h2.9a13 13 0 0 0 0 3zm.8 1.5h2.6a12 12 0 0 0 1.2 3.6A7 7 0 0 1 4.2 13zm2.6-6H4.2A7 7 0 0 1 8 3.4 12 12 0 0 0 6.8 7zM10 16.8c-.7-1-1.3-2.3-1.6-3.8h3.2c-.3 1.5-.9 2.8-1.6 3.8zm1.9-5.3H8.1a11 11 0 0 1 0-3h3.8a11 11 0 0 1 0 3zm.1 5.1a12 12 0 0 0 1.2-3.6h2.6a7 7 0 0 1-3.8 3.6zm1.7-5.1a13 13 0 0 0 0-3h2.9a7 7 0 0 1 0 3z"/></svg>www.hollowbrookleasing.example</li>
      </ul>
    </section>

    <div class="brand">
      <span class="brand-mark" aria-hidden="true"></span>
      <p class="brand-name">Hollowbrook<br>Leasing</p>
    </div>
  </main>
</body>
</html>
```